Fresh & Clean *NEW* BUSINESS CARD Needed - OPTOMETRY Clinic/Optical

High-tech optometry practice with 3 doctors seeking new business card.  We provide eye exams, sell, designer glasses/contacts/specialty eyewear and treat ocular diseases.  For our business cards, we are seeking fresh, clean, and crisp design as we grow our team (staffing change).  Simply adding doctors is making the card look busy/cluttered.
 Looking for professional, less cluttered look yet still have our logo, doctor names, phone, address, and website....If possible!  :)
Names:
Marcia Trelford, O.D.
Ned Pallister, O.D.
Oona Ferrant, O.D.
Phone: 555-014-2738
Website: www.BrightLensHub.example
Address:  417 Garnet R. Holloway, Fernwick, OR 00000
Ultimately we have the main business card with all doctor sames and that card has two versions  (front is always the same).  The back has two designs (1) displays next appointment time/date, (2) for "general use" (non-appointment.)    I have attached what we have used in the past.  
We also need a design template for each team member in our practice with their name, title, and email.   Those should be designed with the "general use" back (see attached).
**Open to entirely new design so don't feel obligated to keep current format.  Need new perspective!  Also including our watermark and some other design features we have consistently used in past in our portfolio.  Included are two options for logos--vertical and horizontal.
**I also would like to remove "Member of Sight Alliance" on our logo if possible**
 Other image files available upon request.

Target Market(s)

New patient & Current Patients

Industry/Entity Type

Optometry

Contact Information for Business Card

High-tech optometry practice with 3 doctors seeking new business card.  We provide eye exams, sell, designer glasses/contacts/specialty eyewear and treat ocular diseases.  For our business cards, we are seeking fresh, clean, and crisp design as we grow our team (staffing change).  Simply adding doctors is making the card look busy/cluttered.  Looking for professional, less cluttered look yet still have our logo, doctor names, phone, address, and website....If possible!  :) Names: Marcia Trelford, O.D. Ned Pallister, O.D. Oona Ferrant, O.D. Phone: 555-014-2738 Website: www.BrightLensHub.example Address:  417 Garnet R. Holloway, Fernwick, OR 00000 Ultimately we have the main business card with all doctor sames and that card has two versions  (front is always the same).  The back has two designs (1) displays next appointment time/date, (2) for "general use" (non-appointment.)    I have attached what we have used in the past.   We also need a design template for each team member in our practice with their name, title, and email.   Those should be designed with the "general use" back (see attached). **Open to entirely new design so don't feel obligated to keep current format.  Need new perspective!  Also including our watermark and some other design features we have consistently used in past in our portfolio.  Included are two options for logos--vertical and horizontal. **I also would like to remove "Member of Sight Alliance" on our logo if possible**  Other image files available upon request.

Font styles to use
Other font styles liked:
• We have used Montserrat / Yellowtail in the past

Colors

Designer to choose colors to be used in the design.

Requirements
Must have
• Clean & Fresh Design with Logo / Info provided in description. Horizontal orientation. **I have included the CMYK colors we currently have in our logo.
Should not have
• Cluttered

```html
<!DOCTYPE html>
<html lang="en">
<head>
<meta charset="utf-8">
<title>BrightLens Hub – Business Cards</title>
<link href="https://fonts.googleapis.com/css2?family=Arimo:wght@400;700&family=Yellowtail&display=swap" rel="stylesheet">
<style>
  :root {
    --backdrop: #2b2b2b;
    --card: #ffffff;
    --slate: #4d6470;
    --ink: #545a60;
    --brand-grey: #636466;
    --gold: #d6a700;
    --aqua: #9fd8e4;
    --rule: #b6bf7c;
  }
  * { margin: 0; padding: 0; box-sizing: border-box; }
  html, body { width: 1200px; height: 840px; overflow: hidden; background: var(--backdrop); }
  body { position: relative; font-family: "Arimo", Arial, sans-serif; }

  .card {
    position: absolute;
    width: 535px;
    height: 305px;
    background: var(--card);
    box-shadow: 0 12px 30px rgba(0,0,0,0.35);
  }
  .card--appointment { left: 185px; top: 92px; border-radius: 34px 0 34px 0; }
  .card--contact { left: 489px; top: 420px; border-radius: 0 34px 0 34px; }

  .brand { position: absolute; left: 330px; top: 123px; width: 190px; text-align: center; }
  .brand__dot {
    display: block; width: 58px; height: 58px; margin: 0 auto 10px;
    border-radius: 50%; background: var(--aqua);
  }
  .brand__name {
    font-family: "Arimo", Arial, sans-serif; font-weight: 400;
    color: var(--brand-grey); font-size: 31px; line-height: 38px; letter-spacing: 0.5px;
  }

  .appt__title { position: absolute; left: 21px; top: 20px; font-size: 16.5px; font-weight: 700; color: var(--slate); }
  .appt__field { position: absolute; left: 21px; width: 358px; display: flex; align-items: flex-end; color: var(--gold); font-weight: 700; font-size: 14.5px; }
  .appt__field--date { top: 63px; }
  .appt__field--time { top: 110px; }
  .appt__dots { flex: 1; margin-left: 5px; border-bottom: 2px dotted var(--gold); height: 1px; margin-bottom: 3px; }
  .appt__notice { position: absolute; left: 21px; top: 143px; font-size: 14.5px; line-height: 18px; color: var(--slate); }

  .doctors { position: absolute; left: 20px; top: 16px; list-style: none; color: var(--gold); }
  .doctors li { font-size: 13.5px; line-height: 23px; }
  .doctors .doctor__name { font-family: "Yellowtail", cursive; font-size: 19px; }

  .address { position: absolute; left: 20px; top: 114px; font-size: 14.5px; line-height: 18px; color: var(--ink); font-style: normal; }
  .divider { position: absolute; left: 20px; top: 163px; width: 223px; height: 1px; background: var(--rule); }
  .contact { position: absolute; left: 20px; top: 175px; list-style: none; color: var(--ink); font-size: 14.5px; }
  .contact li { display: flex; align-items: center; height: 21px; }
  .contact svg { width: 13px; height: 13px; margin-right: 6px; }
</style>
</head>
<body>

<section class="card card--appointment" aria-label="Appointment card">
  <h2 class="appt__title">Your Next Appointment</h2>
  <div class="appt__field appt__field--date">Date <span class="appt__dots"></span></div>
  <div class="appt__field appt__field--time">Time <span class="appt__dots"></span></div>
  <p class="appt__notice">If Your Unable To Keep Your Appointment<br>Kindly Give Us 24 Hour Notice</p>
  <div class="brand">
    <span class="brand__dot"></span>
    <div class="brand__name">brightlens<br>hub</div>
  </div>
</section>

<section class="card card--contact" aria-label="Contact card">
  <ul class="doctors">
    <li><span class="doctor__name">Marcia Trelford</span>, O.D.</li>
    <li><span class="doctor__name">Ned Pallister</span>, O.D.</li>
    <li><span class="doctor__name">Oona Ferrant</span>, O.D.</li>
  </ul>
  <address class="address">417 Garnet R. Holloway<br>Fernwick, OR 00000</address>
  <div class="divider"></div>
  <ul class="contact">
    <li>
      <svg viewBox="0 0 16 16" aria-hidden="true"><path d="M3.5 1.5l2.5 0.5 1 3-1.6 1.3a9 9 0 0 0 4.3 4.3L11 9l3 1 .5 2.5-1.8 1.8C7 14 2 9 1.7 3.3z" fill="none" stroke="#d6a700" stroke-width="1.5" stroke-linejoin="round"/></svg>
      555-014-2738
    </li>
    <li>
      <svg viewBox="0 0 16 16" aria-hidden="true" fill="none" stroke="#d6a700" stroke-width="1.2"><circle cx="8" cy="8" r="6.5"/><ellipse cx="8" cy="8" rx="2.8" ry="6.5"/><path d="M1.5 8h13M2.5 4.8h11M2.5 11.2h11"/></svg>
      www.BrightLensHub.example
    </li>
  </ul>
  <div class="brand">
    <span class="brand__dot"></span>
    <div class="brand__name">brightlens<br>hub</div>
  </div>
</section>

</body>
</html>
```